Startup photography business has a new logo, now we need business cards

Design a business card for the two partners of our business.
Our business Brisk Pelican has a new logo and we need to design a business card to showcase it and us.
Our colours of blue and orange are punchy and vivid, but how can we make the most of it on our card?

It should have our name Brisk Pelican
name of partner
phone number
email
website

Industry/Entity Type

Professional Photography

Contact Information for Business Card

Tom Ashworth
+61 400 55 61 72
tom@briskpelican.com.au
briskpelican.com.au

second card
Neil Porter
+61 400 918 263
tom@briskpelican.com.au
briskpelican.com.au

Colors
f37122
f68d4c
33a6d7
0592cd

Requirements
Must have
• one version of our logo, we have included options
• Name
• phone number
• email
• website
Nice to have
• instagram briskpelicanmedia
• twitter briskpelicanmedia
• facebook briskpelicanmedia

```html
<!DOCTYPE html>
<html lang="en">
<head>
<meta charset="utf-8">
<title>Brisk Pelican – Business Cards</title>
<link href="https://fonts.googleapis.com/css2?family=Arimo:wght@400;700&family=Tinos&display=swap" rel="stylesheet">
<style>
  :root{
    --bg:#e7e3dc;
    --paper:#f7f7f6;
    --ink:#0d0d0d;
    --ink-soft:#2a2a2a;
    --brand-blue:#33a6d7;
    --brand-blue-deep:#0592cd;
    --brand-orange:#f37122;
    --brand-orange-soft:#f68d4c;
    --white:#ffffff;
  }
  *{margin:0;padding:0;box-sizing:border-box}
  html,body{width:1200px;height:902px;overflow:hidden;background:var(--bg)}
  .canvas{position:relative;width:1200px;height:902px}
  .card{position:absolute;width:560px;height:320px;background:var(--paper);
        box-shadow:0 6px 18px rgba(0,0,0,.18);overflow:hidden}
  .card--front{left:80px;top:90px}
  .card--back{left:560px;top:492px}

  .brand-mark{position:absolute;display:flex;align-items:center;gap:14px;
              font-family:"Arimo",sans-serif;font-weight:700;color:var(--brand-blue);
              text-transform:uppercase;letter-spacing:1px;white-space:nowrap}
  .brand-mark__dot{border-radius:50%;background:var(--brand-orange);flex:none}
  .card--front .brand-mark{left:50%;top:50%;transform:translate(-50%,-50%);font-size:42px}
  .card--front .brand-mark__dot{width:64px;height:64px}
  .card--back .brand-mark{left:24px;top:188px;font-size:24px;gap:10px}
  .card--back .brand-mark__dot{width:38px;height:38px}

  .card__panels{position:absolute;inset:0}
  .holder-name{position:absolute;right:34px;top:44px;font-family:"Tinos",serif;
               font-weight:400;font-size:30px;color:var(--brand-orange);white-space:nowrap}
  .contact-list{position:absolute;right:20px;top:154px;list-style:none;
                font-family:"Arimo",sans-serif;font-size:13px;color:var(--white)}
  .contact-list li{display:flex;justify-content:flex-end;align-items:center;gap:10px;height:24px}
  .contact-list .icon{width:16px;height:16px;flex:none}
  .contact-list .social{margin-top:8px;gap:6px}
  .contact-list .social-box{width:14px;height:14px;background:var(--white);border-radius:2px}
  .contact-list .handle{margin-top:2px}
</style>
</head>
<body>
<main class="canvas">

  <section class="card card--front" aria-label="Card front">
    <div class="brand-mark"><span class="brand-mark__dot"></span>Brisk Pelican</div>
  </section>

  <section class="card card--back" aria-label="Card back">
    <svg class="card__panels" width="560" height="320" viewBox="0 0 560 320" aria-hidden="true">
      <polygon points="170,0 560,0 560,96 330,182" fill="var(--ink)"/>
      <polygon points="330,182 560,96 560,320 356,320" fill="var(--brand-blue)"/>
      <line x1="150" y1="0" x2="330" y2="178" stroke="var(--brand-orange)" stroke-width="5"/>
      <line x1="330" y1="182" x2="356" y2="320" stroke="var(--ink)" stroke-width="6"/>
    </svg>

    <div class="brand-mark"><span class="brand-mark__dot"></span>Brisk Pelican</div>

    <h1 class="holder-name">Tom Ashworth</h1>

    <ul class="contact-list">
      <li>+61 400 55 61 72
        <svg class="icon" viewBox="0 0 16 16"><rect width="16" height="16" rx="2" fill="#fff"/><path d="M5 3.5l2 2-1 1.3c.6 1.3 1.6 2.3 2.9 2.9l1.3-1 2 2-1.2 1.8C7.5 12.4 3.6 8.5 3.3 5z" fill="var(--ink-soft)"/></svg>
      </li>
      <li>briskpelican.com.au
        <svg class="icon" viewBox="0 0 16 16"><rect width="16" height="16" rx="2" fill="#fff"/><circle cx="8" cy="8" r="5" fill="none" stroke="var(--ink-soft)" stroke-width="1.2"/><ellipse cx="8" cy="8" rx="2.2" ry="5" fill="none" stroke="var(--ink-soft)" stroke-width="1"/><line x1="3" y1="8" x2="13" y2="8" stroke="var(--ink-soft)" stroke-width="1"/></svg>
      </li>
      <li>tom@briskpelican.com.au
        <svg class="icon" viewBox="0 0 16 16"><rect width="16" height="16" rx="2" fill="#fff"/><rect x="3" y="4.5" width="10" height="7" fill="none" stroke="var(--ink-soft)" stroke-width="1.2"/><path d="M3 4.5l5 4 5-4" fill="none" stroke="var(--ink-soft)" stroke-width="1.2"/></svg>
      </li>
      <li class="social"><span class="social-box"></span><span class="social-box"></span><span class="social-box"></span></li>
      <li class="handle">briskpelicanmedia</li>
    </ul>
  </section>

</main>
</body>
</html>
```